CREATE R&B MIXTAPE COVER !!
Hi , my name is Brontel , and I want you to create a cover for my music mixtape.
The name of the mixtape is Tormenta , and has these types of music :
- R&B
- Hiphop
- Afrohouse
- Dancehall
- Reggaeton
In the attachments you’ll find two backgrounds. One with a lightning bolt , and a grey one with a stroke in the middle. I like both very much , but don’t know which one to choose. That’s why I want to compare the end results of both , and then make a decision. Below you’ll find instructions for both backgrounds.
If you think you can make something better for me , you can also try to do your own thing , and use your own background for example.
Instructions for the first background ( Lightning bolt )
I would like you to design my name ‘Brontel’ into / onto the lightning bolt. I want the lightning bolt + my name to be my DJ Logo , but my name doesn’t have to be in very big letters. Tormenta is the name of the mixtape and has to be in big letters. I was thinking above the logo.
Then there are 2 remaining sentences : ‘Mixed by DJ Brontel’ and ‘Mixtape Volume 1’. These two sentences have to be smaller than ‘Tormenta’. You can put them under the logo.
Instructions for the second background ( Grey )
I would like you to create a logo of my whole name ‘Brontel’ Or just with the letter V. You can put the logo above the stroke.
The mixtape name ‘Tormenta’ has to be in the middle in big letters.
Then there are 2 remaining sentences : ‘Mixed by DJ Brontel’ and ‘Mixtape Volume 1’. These two have to be smaller than ‘Tormenta’ in the middle. I want these sentences below.
Use your imagination with the name Tormenta , the two sentences and the logo. I want it to look professional and unique.
Kind regards ,
Brontel

```html
<!DOCTYPE html>
<html lang="en">
<head>
<meta charset="utf-8">
<title>Tormenta – Mixtape Volume 1</title>
<link rel="stylesheet" href="https://fonts.googleapis.com/css2?family=Metal+Mania&family=Open+Sans:wght@400;600&display=swap">
<style>
  :root {
    --bg-dark: #151515;
    --bg-mid: #2b2b2b;
    --bg-light: #3a3a3a;
    --band-dark: #1e1e1e;
    --band-light: #3c3c3c;
    --accent: #35c6f2;
    --accent-glow: rgba(40, 180, 255, 0.9);
    --logo: #cfefff;
    --text: #ffffff;
  }
  html, body {
    margin: 0;
    padding: 0;
    width: 1200px;
    height: 1200px;
    overflow: hidden;
    background: var(--bg-dark);
  }
  .cover {
    position: relative;
    width: 1200px;
    height: 1200px;
    overflow: hidden;
    background:
      radial-gradient(ellipse 70% 60% at 50% 35%, rgba(255,255,255,0.08), rgba(0,0,0,0) 70%),
      radial-gradient(ellipse 90% 90% at 50% 50%, rgba(0,0,0,0) 45%, rgba(0,0,0,0.65) 100%),
      repeating-linear-gradient(180deg, rgba(255,255,255,0.025) 0 2px, rgba(0,0,0,0.05) 2px 5px),
      linear-gradient(180deg, var(--bg-light), var(--bg-mid) 50%, var(--bg-dark));
  }
  .brand {
    position: absolute;
    top: 170px;
    left: 0;
    width: 100%;
    text-align: center;
    font-family: "Metal Mania", fantasy;
    font-size: 92px;
    letter-spacing: 4px;
    color: var(--logo);
    line-height: 1;
  }
  .title-band {
    position: absolute;
    left: 0;
    top: 410px;
    width: 100%;
    height: 320px;
    background:
      linear-gradient(90deg, rgba(0,0,0,0.35), rgba(0,0,0,0) 30%, rgba(0,0,0,0) 70%, rgba(0,0,0,0.35)),
      repeating-linear-gradient(180deg, rgba(255,255,255,0.03) 0 2px, rgba(0,0,0,0.06) 2px 5px),
      linear-gradient(180deg, var(--band-dark) 0%, var(--band-light) 18%, var(--band-light) 82%, var(--band-dark) 100%);
  }
  .glow-line {
    position: absolute;
    left: 50%;
    width: 760px;
    height: 6px;
    transform: translateX(-50%);
    border-radius: 3px;
    background: linear-gradient(90deg, rgba(40,180,255,0), var(--accent-glow) 35%, #bff0ff 50%, var(--accent-glow) 65%, rgba(40,180,255,0));
    box-shadow: 0 0 24px 6px rgba(30,160,255,0.55), 0 0 70px 18px rgba(30,140,255,0.25);
  }
  .glow-line--top { top: 74px; }
  .glow-line--bottom { top: 300px; }
  .mixtape-title {
    position: absolute;
    left: 0;
    top: 118px;
    width: 100%;
    margin: 0;
    text-align: center;
    font-family: "Metal Mania", fantasy;
    font-weight: 400;
    font-size: 168px;
    line-height: 1;
    letter-spacing: 8px;
    color: var(--accent);
    text-shadow: 0 0 18px rgba(40,180,255,0.35);
  }
  .credits {
    position: absolute;
    left: 0;
    top: 1016px;
    width: 100%;
    text-align: center;
    color: var(--text);
    font-family: "Open Sans", sans-serif;
  }
  .credits__mixed {
    margin: 0;
    font-size: 40px;
    font-weight: 400;
  }
  .credits__volume {
    margin: 30px 0 0;
    font-size: 28px;
    letter-spacing: 9px;
  }
</style>
</head>
<body>
  <main class="cover">
    <div class="brand">Brontel</div>
    <section class="title-band">
      <div class="glow-line glow-line--top"></div>
      <h1 class="mixtape-title">TORMENTA</h1>
      <div class="glow-line glow-line--bottom"></div>
    </section>
    <footer class="credits">
      <p class="credits__mixed">Mixed by DJ Brontel</p>
      <p class="credits__volume">Mixtape Volume 1</p>
    </footer>
  </main>
</body>
</html>
```